W need a Menu Board designed for a" make your own poke bowl" and Sushi Menu. We would like our logo & Colors to be intergraded with the menu . Also will need to be able to adjust the pricing in the future as needed.

```html
<!DOCTYPE html>
<html lang="en">
<head>
<meta charset="utf-8">
<title>Sushi &amp; Poke Menu</title>
<link href="https://fonts.googleapis.com/css2?family=Alegreya:wght@400;500;700&family=Lobster&family=Montserrat:wght@500&display=swap" rel="stylesheet">
<style>
:root{
  --backdrop:#d9dadc;
  --paper:#eeeeed;
  --ink:#1b1b1b;
  --blue:#1f50a6;
  --blue-light:#6b9fd3;
  --banner-text:#ffffff;
}
*{margin:0;padding:0;box-sizing:border-box}
html,body{width:1200px;height:813px;overflow:hidden;background:var(--backdrop)}
body{position:relative;font-family:"Alegreya",Georgia,serif;color:var(--ink)}
.page{position:absolute;top:20px;width:560px;height:773px;background:var(--paper);overflow:hidden}
.page--sushi{left:20px}
.page--poke{left:620px}
.abs{position:absolute}
.art{position:absolute;border-radius:6px}
.title{left:0;right:0;top:18px;text-align:center;font-family:"Lobster",cursive;font-size:66px;line-height:1;color:var(--blue)}
.subtitle{left:0;right:0;top:86px;text-align:center;font-family:"Montserrat",sans-serif;font-weight:500;font-size:34px;letter-spacing:1px;color:var(--blue-light);line-height:1}
.banner{position:absolute;left:50%;transform:translateX(-50%);display:flex;align-items:center;justify-content:center}
.banner svg{position:absolute;inset:0;width:100%;height:100%}
.banner span{position:relative;color:var(--banner-text);font-weight:500;line-height:1}
.rows{position:absolute;list-style:none}
.rows li{display:flex;justify-content:space-between;font-weight:700;font-size:11.5px;height:22.3px;align-items:flex-start}
.rows small{font-weight:400;font-size:7px}
.rows .desc{display:block;font-weight:400;font-size:6.4px;line-height:1.35;margin-top:1px}
.rows li.tall{height:54px}
.divider{position:absolute;width:1px;background:var(--ink)}
.brand{position:absolute;left:0;right:0;text-align:center;font-family:"Alegreya",serif;font-weight:700;color:var(--blue);line-height:1}
.head{position:absolute;font-weight:700;font-size:12px}
.bullets{position:absolute;list-style:none;font-size:10.5px;line-height:15.5px}
.bullets li::before{content:"\2022";margin-right:6px}
.price-start{left:0;right:0;top:74px;text-align:center;font-weight:700;font-size:16px;color:var(--blue)}
.prices{position:absolute;list-style:none;font-size:10.5px}
.prices li{display:flex;justify-content:space-between;height:17.5px}
</style>
</head>
<body>

<section class="page page--sushi">
  <div class="art" style="left:18px;top:60px;width:120px;height:70px;background:radial-gradient(ellipse,#f0b89a 0%,#eeeeed 75%)" role="img" aria-label="Illustration of nigiri, ginger and lemon slices"></div>
  <div class="art" style="left:420px;top:40px;width:120px;height:90px;background:radial-gradient(ellipse,#4a4f4a 0%,#eeeeed 75%)" role="img" aria-label="Illustration of sushi rolls with herbs and wasabi"></div>
  <h1 class="abs title">Menú</h1>
  <p class="abs subtitle">RESTAURANT</p>

  <div class="banner" style="top:144px;width:180px;height:24px">
    <svg viewBox="0 0 180 24" preserveAspectRatio="none" aria-hidden="true"><path d="M4 3 L176 1 L170 7 L180 12 L172 17 L178 23 L2 22 L8 16 L0 11 L7 6 Z" fill="var(--blue)"/></svg>
    <span style="font-size:17px">Sushi Rolls</span>
  </div>

  <ul class="rows" style="left:52px;top:186px;width:205px">
    <li><span>Tuna Tartar</span><span>$24.99</span></li>
    <li><span>Salmon Tartar</span><span>$22.99</span></li>
    <li><span>Tuna Tower</span><span>$16.99</span></li>
    <li><span>Salmon Tower</span><span>$16.99</span></li>
    <li><span>Kani Salad</span><span>$18.99</span></li>
    <li><span>Tuna Tataki</span><span>$00.00</span></li>
    <li><span>California Roll</span><span>$9.99</span></li>
    <li><span>Avocado Roll</span><span>$7.99</span></li>
    <li><span>Tuna Roll (Small)</span><span>$9.99</span></li>
    <li><span>Salmon Roll (Small)</span><span>$9.99</span></li>
    <li><span>Cucumber Roll</span><span>$7.99</span></li>
    <li><span>Veggie Roll</span><span>$9.99</span></li>
  </ul>
  <div class="divider" style="left:275px;top:186px;height:258px"></div>
  <ul class="rows" style="left:292px;top:188px;width:220px">
    <li style="height:27px"><span>Salmon Avocado Roll</span><span>$9.99</span></li>
    <li style="height:27px"><span>Salmon Avocado <small>w/ Salmon on Top</small></span><span>$14.99</span></li>
    <li style="height:27px"><span>Salmon Avocado <small>w/ Tuna on Top</small></span><span>$14.99</span></li>
    <li style="height:27px"><span>Tuna Avocado <small>w/ Tuna on Top</small></span><span>$14.99</span></li>
    <li style="height:27px"><span>Tuna Avocado <small>w/ Salmon on Top</small></span><span>$14.99</span></li>
    <li style="height:27px"><span>Spicy Tuna Roll</span><span>$9.99</span></li>
    <li class="tall"><span>Kali Roll<span class="desc">(Inside Out w/ Kani, Cucumber, Avocado,<br>&amp; Tempura Flakes Topped w/ Salmon<br>&amp; Dressed with Eel Sauce)</span></span><span>$14.99</span></li>
    <li class="tall"><span>Rikki Roll<span class="desc">(Inside Out w/ Kani, Cucumber &amp; Cilantro<br>Topped w/ Hamachi, Jalapeno &amp; Dressed<br>w/ Cilantro Truffle Sauce)</span></span><span>$15.99</span></li>
  </ul>

  <div class="banner" style="top:464px;width:176px;height:24px">
    <svg viewBox="0 0 180 24" preserveAspectRatio="none" aria-hidden="true"><path d="M4 3 L176 1 L170 7 L180 12 L172 17 L178 23 L2 22 L8 16 L0 11 L7 6 Z" fill="var(--blue)"/></svg>
    <span style="font-size:17px">Negri</span>
  </div>
  <ul class="rows" style="left:56px;top:505px;width:200px">
    <li><span>Salmon</span><span>$00.00</span></li>
    <li><span>Ahi</span><span>$00.00</span></li>
    <li><span>Wahoo</span><span>$00.00</span></li>
  </ul>
  <ul class="rows" style="left:295px;top:505px;width:212px">
    <li><span>Hamachi</span><span>$00.00</span></li>
    <li><span>Toro</span><span>$00.00</span></li>
  </ul>

  <div class="art" style="left:0;right:0;bottom:0;height:110px;border-radius:0;background:linear-gradient(90deg,#d9927f,#e8704a 35%,#c9b98c 55%,#c98a86 75%,#8a6b5e)" role="img" aria-label="Illustration of seafood: octopus, mussels, prawn, squid and a bowl of sauce"></div>
  <div class="art" style="left:0;top:575px;width:100px;height:90px;background:radial-gradient(ellipse,#d9c3a8 0%,#eeeeed 75%)" role="img" aria-label="Illustration of a wooden spoon with salt and herbs"></div>
  <div class="art" style="right:0;top:575px;width:100px;height:90px;background:radial-gradient(ellipse,#e8a27a 0%,#eeeeed 75%)" role="img" aria-label="Illustration of shellfish and peppers"></div>
  <p class="brand" style="top:610px;font-size:30px">Tideline</p>
  <p class="brand" style="top:644px;font-size:11px;letter-spacing:2px">FISH HOUSE</p>
</section>

<section class="page page--poke">
  <div class="art" style="right:0;top:0;width:110px;height:115px;background:radial-gradient(circle,#7a8f5a 0%,#c96a4a 45%,#eeeeed 75%)" role="img" aria-label="Photo of a poke bowl with salmon, avocado and cucumber"></div>
  <div class="art" style="right:0;top:282px;width:90px;height:80px;background:radial-gradient(circle,#e8744e 0%,#eeeeed 72%)" role="img" aria-label="Photo of a salmon poke bowl"></div>
  <div class="art" style="left:146px;top:400px;width:76px;height:76px;border-radius:50%;background:radial-gradient(circle,#d67a5a,#9fbf7a 60%,#e6e6e6)" role="img" aria-label="Photo of a poke bowl with tuna and vegetables"></div>

  <div class="banner" style="top:36px;width:260px;height:36px">
    <svg viewBox="0 0 180 24" preserveAspectRatio="none" aria-hidden="true"><path d="M4 3 L176 1 L170 7 L180 12 L172 17 L178 23 L2 22 L8 16 L0 11 L7 6 Z" fill="var(--blue)"/></svg>
    <span style="font-size:25px">Poke Bowls</span>
  </div>
  <p class="abs price-start">Starting Price $15.99</p>

  <p class="head" style="left:30px;top:108px">Choice 1 Base:</p>
  <ul class="bullets" style="left:30px;top:130px">
    <li>White Rice</li><li>Brown Rice</li><li>Quinoa</li><li>Zucchini Noodles</li><li>Lettuce</li>
  </ul>
  <p class="head" style="left:185px;top:106px">Choice 1 Protein:</p>
  <ul class="bullets" style="left:195px;top:128px">
    <li>Tuna Poke</li><li>Salmon Poke</li><li>Spicy Tuna</li><li>Spicy Salmon</li><li>Kani</li><li>Wahoo</li>
  </ul>
  <p class="head" style="left:340px;top:106px">Choice 1 Crunch:</p>
  <ul class="bullets" style="left:350px;top:125px">
    <li>Tempura Flakes</li><li>Toasted Shredded Nori</li><li>Toasted Sesame</li>
  </ul>

  <p class="head" style="left:30px;top:218px">Choose 4 Toppings:</p>
  <ul class="bullets" style="left:30px;top:240px">
    <li>Asian Slaw</li><li>Edamame</li><li>Red Onion</li><li>Red Cabbage</li><li>Jalapeno</li>
  </ul>
  <ul class="bullets" style="left:195px;top:240px">
    <li>Scallions</li><li>Carrot</li><li>Radish</li><li>Cucumber</li><li>Tomato</li>
  </ul>
  <ul class="bullets" style="left:350px;top:240px">
    <li>Sprout</li><li>Cilantro</li><li>Pickled Ginger</li>
  </ul>

  <div class="banner" style="top:337px;width:220px;height:26px">
    <svg viewBox="0 0 180 24" preserveAspectRatio="none" aria-hidden="true"><path d="M4 3 L176 1 L170 7 L180 12 L172 17 L178 23 L2 22 L8 16 L0 11 L7 6 Z" fill="var(--blue)"/></svg>
    <span style="font-size:16px">Prem Toppings:</span>
  </div>
  <ul class="prices" style="left:30px;top:370px;width:150px">
    <li><span>Avocado</span><span>$2.00</span></li>
    <li><span>Seaweed Salad</span><span>$1.00</span></li>
    <li><span>Edamame</span><span>$1.00</span></li>
  </ul>
  <ul class="prices" style="left:240px;top:370px;width:200px">
    <li><span>Mango</span><span>$1.00</span></li>
    <li><span>Pineapple</span><span>$1.00</span></li>
  </ul>

  <p class="head" style="left:30px;top:428px">Sauces:</p>
  <ul class="bullets" style="left:30px;top:448px;line-height:17.5px">
    <li>Spicy Mayo</li><li>Sweet Chili</li><li>Sriracha</li>
  </ul>
  <ul class="bullets" style="left:195px;top:444px;line-height:17.5px">
    <li>Ponzu</li><li>Eel Sauce</li><li>Cilantro Garlic Aioli</li>
  </ul>
  <ul class="bullets" style="left:350px;top:438px;line-height:17.5px">
    <li>Basil Aioli</li><li>Sesame Ginger</li><li>Carrot Honey Ginger</li>
  </ul>

  <div class="banner" style="top:510px;width:280px;height:26px">
    <svg viewBox="0 0 180 24" preserveAspectRatio="none" aria-hidden="true"><path d="M4 3 L176 1 L170 7 L180 12 L172 17 L178 23 L2 22 L8 16 L0 11 L7 6 Z" fill="var(--blue)"/></svg>
    <span style="font-size:16px">Additional Protein Scoop:</span>
  </div>
  <ul class="prices" style="left:30px;top:545px;width:150px">
    <li><span>Tuna Poke</span><span>$4.00</span></li>
    <li><span>Salmon Poke</span><span>$4.00</span></li>
    <li><span>Spicy Tuna</span><span>$4.00</span></li>
  </ul>
  <ul class="prices" style="left:240px;top:545px;width:200px">
    <li><span>Spicy Salmon</span><span>$4.00</span></li>
    <li><span>Kani</span><span>$4.00</span></li>
  </ul>

  <div class="art" style="left:40px;top:620px;width:140px;height:95px;background:radial-gradient(ellipse,#e0874f 0%,#9fb86a 55%,#eeeeed 78%)" role="img" aria-label="Photo of grilled salmon steak with asparagus and lime"></div>
  <div class="art" style="left:230px;top:598px;width:80px;height:80px;border-radius:50%;background:radial-gradient(circle,#c97a55,#7ea25a 60%,#f4f4f4)" role="img" aria-label="Photo of a salmon salad plate"></div>
  <div class="art" style="left:360px;top:610px;width:170px;height:140px;background:radial-gradient(circle,#e7c79a 0%,#b77a4a 55%,#eeeeed 75%)" role="img" aria-label="Photo of a bowl with rice, shrimp, radish and carrot, with chopsticks"></div>
  <p class="brand" style="top:700px;left:60px;right:auto;width:200px;font-size:30px">Tideline</p>
  <p class="brand" style="top:734px;left:60px;right:auto;width:200px;font-size:11px;letter-spacing:2px">FISH HOUSE</p>
</section>

</body>
</html>
```